Wedding Program

Miriam and Owen are getting married. They are looking for a simple 4-page program that conveys the special day. Venue is a museum in a large East-Coast city: classic 18th century, formal. Ceremony is non-religious. Party includes a photo booth and DJ.

He's a math geek - she's an activist/educator.

Please incorporate unique design sensibility - be creative! Colors of purple, eggplant, ivory, and gray are the couple's choice. Fall motif OK.

Target Market(s)

ages 25 - 85, members of a family

Industry/Entity Type

Graphic Design

Font styles to use
Serif
Decorative

Colors
8769ae
b7a5cd
fece3e
f78f20
757575
cfcfcf
6b449b
a64599
fffaee

Requirements
Must have
• Readable, attractive 4-color design using the copy and image provided in the attachment.
Nice to have
• It's a LOVE-ly day for a wedding - be creative!
Should not have
• Avoid flowery girly-girl fonts or obvious hearts and flowers stuff.

```html
<!DOCTYPE html>
<html lang="en">
<head>
<meta charset="utf-8">
<title>Wedding Program</title>
<link rel="stylesheet" href="https://fonts.googleapis.com/css2?family=Aleo:wght@300;400;700&display=swap">
<style>
:root{
  --canvas:#ffffff;
  --ivory:#f6f2ec;
  --purple:#6b449b;
  --lavender:#8769ae;
  --lilac:#b7a5cd;
  --plum:#a64599;
  --gold:#fece3e;
  --gray:#5f5f5f;
}
*{margin:0;padding:0;box-sizing:border-box}
html,body{width:1200px;height:900px;overflow:hidden;background:var(--canvas)}
body{position:relative;font-family:"Aleo",Georgia,serif;color:var(--gray)}
.page{position:absolute;top:188px;width:262px;background:var(--ivory);text-align:center;overflow:hidden}
.page--cover{left:33px;height:355px}
.page--party{left:317px;height:412px}
.page--ceremony{left:611px;height:467px}
.page--guests{left:905px;height:523px}

/* cover */
.emblem{position:absolute;left:86px;top:30px;width:86px;height:86px;border-radius:50%;background:var(--gold)}
.couple{position:absolute;left:0;right:0;top:143px;font-size:11px;line-height:14px;color:var(--purple)}
.couple .name{color:var(--gold);font-weight:700;text-transform:uppercase}
.headline{position:absolute;left:0;right:0;top:178px;font-size:45px;font-weight:700;color:var(--purple);letter-spacing:.5px;line-height:48px}
.date{position:absolute;left:44px;top:252px;width:60px;text-align:center;color:var(--purple);font-weight:700}
.date .small{font-size:8px;letter-spacing:1.6px;line-height:11px;display:block}
.date .day{font-size:50px;font-weight:300;color:var(--gold);line-height:44px;display:block;letter-spacing:-2px}
.date .time{font-size:7.5px;line-height:10px;display:block;letter-spacing:.5px}
.divider{position:absolute;left:108px;top:254px;width:2px;height:82px;background:var(--gold)}
.venue{position:absolute;left:120px;top:252px;text-align:left;font-size:16.5px;font-weight:300;line-height:21px;color:var(--purple);white-space:nowrap}

/* party */
.roles{position:absolute;left:0;right:0;top:27px;font-size:10px;line-height:12.5px}
.role{margin-bottom:12px}
.role dt{font-weight:700}
.role dd{color:var(--gray);white-space:nowrap;letter-spacing:-.1px}
.c-plum{color:var(--plum)}
.c-purple{color:var(--purple)}
.c-lav{color:var(--lavender)}
.c-lilac{color:var(--lilac)}
.page-title{position:absolute;left:0;right:0;font-size:12.5px;font-weight:700;text-transform:uppercase}
.page--party .page-title{top:377px;color:var(--lavender)}
.page--ceremony .page-title{top:432px;color:var(--plum)}
.page--guests .page-title{top:489px;color:var(--lilac)}

/* ceremony */
.order{position:absolute;left:0;right:0;top:27px;list-style:none;font-size:10px;line-height:12px}
.order li{margin-bottom:12.3px}
.order .heart{color:var(--purple);font-size:8px;margin-right:3px}

/* guests */
.letter{position:absolute;left:14px;right:14px;top:27px;font-size:10px;line-height:17.5px}
.letter p{margin-bottom:17.5px}
.photo{position:absolute;left:0;top:292px;width:262px;height:110px;background:linear-gradient(100deg,#3f5a2a 0%,#6c7b3a 30%,#4b3a3e 55%,#5b4540 80%,#6e7a8a 100%)}
</style>
</head>
<body>

<section class="page page--cover">
  <div class="emblem" aria-hidden="true"></div>
  <p class="couple"><span class="name">Miriam Alder</span> and <span class="name">Owen Whitcombe</span><br>welcome you to their</p>
  <h1 class="headline">WEDDING</h1>
  <p class="date">
    <span class="small">Saturday</span>
    <span class="small">November</span>
    <span class="day">01</span>
    <span class="time">At 6 p.m.</span>
    <span class="time">in the evening</span>
  </p>
  <div class="divider"></div>
  <p class="venue">The Academy<br>of Sciences<br>Philadelphia<br>Pennsylvania</p>
</section>

<section class="page page--party">
  <dl class="roles">
    <div class="role"><dt class="c-plum">Bride and Groom:</dt><dd>Miriam Alder and Owen Whitcombe</dd></div>
    <div class="role"><dt class="c-purple">Bride's Parents:</dt><dd>Dale and Lorraine Alder</dd></div>
    <div class="role"><dt class="c-lav">Groom's Parents:</dt><dd>Walter</dd></div>
    <div class="role"><dt class="c-lilac">Bridesmaids:</dt><dd>Nora Whitcombe, Tessa Maren, Julia Brandt</dd></div>
    <div class="role"><dt class="c-plum">Groomsmen:</dt><dd>Cole Whitcombe, Peter Alder, Evan Hart, Ravi Das</dd></div>
    <div class="role"><dt class="c-purple">Grandparent of the Bride:</dt><dd>Beatrice Kowalcyk</dd></div>
    <div class="role"><dt class="c-lav">Grandparents of the Groom:</dt><dd>Henry Whitcombe, Arthur Dunmore, June Whitcombe</dd></div>
    <div class="role"><dt class="c-lilac">Celebrant:</dt><dd>Clara Ferris</dd></div>
  </dl>
  <h2 class="page-title">The Wedding Party</h2>
</section>

<section class="page page--ceremony">
  <ol class="order">
    <li><span class="heart">♥</span>Greeting</li>
    <li><span class="heart">♥</span>Ring Blessing</li>
    <li><span class="heart">♥</span>Presentation of the Bride and Groom</li>
    <li><span class="heart">♥</span>Reading: Thomas Reid Calloway, The Orchards of<br>Larkin Valley</li>
    <li><span class="heart">♥</span>Wedding Vows</li>
    <li><span class="heart">♥</span>Exchange of Wedding Rings</li>
    <li><span class="heart">♥</span>Wine Box Ceremony</li>
    <li><span class="heart">♥</span>Signing of Marriage Certificate</li>
    <li><span class="heart">♥</span>Declaration of Support</li>
    <li><span class="heart">♥</span>Reading: Daniel Ashford, The Road Toward Always</li>
    <li><span class="heart">♥</span>Declaration of Marriage</li>
  </ol>
  <h2 class="page-title">The Ceremony</h2>
</section>

<section class="page page--guests">
  <div class="letter">
    <p>Your presence here adds greatly to our joy and happiness on this special day.</p>
    <p>Today marks the beginning of our lives together. We stand before you now, declaring our love for each other and for our intent to be joined in marriage. We share with each other without reservation our lives, fortunes and future.</p>
    <p>We hope that you will continue to wish us well in our new life and we are grateful to have your love, care and best wishes for today and always!</p>
  </div>
  <div class="photo" role="img" aria-label="Photo of the couple together outdoors among green foliage"></div>
  <h2 class="page-title">To Our Wedding Guests</h2>
</section>

</body>
</html>
```